UK Glass Restoration Company needs a Direct Mail Postcard Design

We need a HARD HITTING, COMPELLING 300dpi Camera Ready double sided postcard.
The dimensions will be 109mm x 152mm including bleed. We are a scratched glass repair / etched graffiti removal glass restoration company based in London, UK.
We operate mainly within the construction and commercial marketplace, however this particular postcard design is aimed solely at shop owners who have become victims of vandalism, due to etched graffiti tags and or scratches being left on their shop front glass.
We wish to focus the shop / business owners mind to the negative impact such vandalism has on the image of their business and how we are able to offer a quick and cost effective solution
We will supply text for both sides of the postcard along with relevant images, company logo and previous flyer designs, however we are happy for the selected designer to source suitable alternative images provided they are in keeping with the exact "Before" and "After" theme.
The finished postcard must preferably have a white background, but again we are open to creative suggestions.
Target Market(s)
UK SHOP OWNERS
Industry/Entity Type
It Company

```html
<!DOCTYPE html>
<html lang="en">
<head>
<meta charset="utf-8">
<title>Lucent Glass Repairs – Postcard</title>
<link rel="stylesheet" href="https://fonts.googleapis.com/css2?family=Anton&family=Roboto+Condensed:wght@700&family=Open+Sans:wght@400;700&display=swap">
<style>
  :root {
    --backdrop: #5b5b5b;
    --card: #ffffff;
    --panel-top: #f4f4f4;
    --panel-bottom: #d6d6d6;
    --brand-blue: #2aa9e8;
    --brand-blue-dark: #1279b8;
    --sky: #45b8f0;
    --ink: #1a1a1a;
    --alert-red: #e0161b;
    --photo-warm-1: #7a5a34;
    --photo-warm-2: #3b2a18;
    --photo-cool-1: #b9c2c6;
    --photo-cool-2: #6a6c66;
  }
  * { box-sizing: border-box; margin: 0; padding: 0; }
  html, body { width: 1200px; height: 900px; overflow: hidden; }
  body { background: var(--backdrop); font-family: "Open Sans", Arial, sans-serif; position: relative; }

  .postcard {
    position: absolute; top: 72px; width: 530px; height: 755px;
    background: linear-gradient(var(--panel-top) 55%, var(--panel-bottom) 95%);
    overflow: hidden;
  }
  .postcard--front { left: 50px; }
  .postcard--back { left: 620px; }

  .photo { position: absolute; left: 0; top: 0; width: 530px; }
  .photo--before { height: 390px; background: radial-gradient(circle at 40% 35%, var(--photo-warm-1), var(--photo-warm-2)); }
  .photo--after { height: 330px; background: linear-gradient(160deg, var(--photo-cool-1), var(--photo-cool-2)); }

  .panel-curve { position: absolute; left: 0; width: 530px; }

  .pointer-arrow { position: absolute; left: 85px; top: 150px; width: 140px; height: 170px; }

  .stage-tag {
    position: absolute; width: 230px; height: 70px; text-align: center;
    background: linear-gradient(var(--sky), var(--brand-blue));
    border-radius: 4px; color: #fff;
    font-family: "Roboto Condensed", Arial, sans-serif; font-weight: 700;
    box-shadow: 0 3px 5px rgba(0,0,0,.35);
  }
  .stage-tag::before, .stage-tag::after {
    content: ""; position: absolute; top: -8px; border-bottom: 8px solid var(--brand-blue-dark);
  }
  .stage-tag::before { left: -10px; border-left: 10px solid transparent; }
  .stage-tag::after { right: -10px; border-right: 10px solid transparent; }
  .stage-tag__title { font-size: 27px; line-height: 34px; padding-top: 2px; }
  .stage-tag__sub { font-size: 22px; line-height: 26px; color: var(--ink); }
  .stage-tag--before { left: 150px; top: 306px; }
  .stage-tag--after { left: 150px; top: 258px; }

  .headline {
    position: absolute; left: 0; top: 392px; width: 530px; text-align: center;
    font-family: "Anton", Impact, sans-serif; color: var(--ink);
    text-transform: uppercase; letter-spacing: .5px;
  }
  .headline__line { display: block; font-size: 46px; line-height: 54px; }
  .headline__accent { color: var(--alert-red); font-style: italic; display: inline-block; transform: rotate(-4deg); font-size: 48px; }

  .intro-box {
    position: absolute; left: 18px; top: 518px; width: 494px; height: 114px;
    background: var(--sky); border-radius: 14px; padding: 8px 12px;
    color: var(--ink); font-size: 12.4px; line-height: 16.6px; text-align: justify;
    box-shadow: 0 6px 8px rgba(0,0,0,.25);
  }
  .intro-box strong { font-weight: 700; }
  .intro-box .call-line { color: #fff; font-weight: 700; }

  .benefits { position: absolute; left: 25px; top: 350px; width: 478px; }
  .benefits__title {
    font-family: "Roboto Condensed", Arial, sans-serif; font-weight: 700;
    color: var(--alert-red); font-size: 16px; margin-bottom: 8px;
  }
  .benefits__list { list-style: none; }
  .benefits__list li {
    position: relative; padding-left: 16px; font-size: 12.8px; line-height: 17px;
    color: var(--ink); margin-bottom: 2px;
  }
  .benefits__list li::before {
    content: ""; position: absolute; left: 2px; top: 6px; width: 6px; height: 6px;
    border-radius: 50%; background: var(--alert-red);
  }
  .benefits__list li.benefit--strong { font-size: 13.2px; }
  .benefits__list strong { font-size: 14.5px; }

  .coupon {
    position: absolute; left: 40px; top: 566px; width: 455px; height: 110px;
    background: var(--sky); border-radius: 14px 14px 0 0;
  }
  .coupon__badge {
    position: absolute; left: 10px; top: 13px; width: 155px; height: 60px;
    border: 2px solid var(--alert-red); border-radius: 26px;
    background: linear-gradient(var(--sky), var(--brand-blue));
    font-family: "Anton", Impact, sans-serif; font-size: 31px; line-height: 56px;
    text-align: center; color: var(--ink);
  }
  .coupon__badge-save { color: #fff; text-shadow: 1px 1px 0 #333, -1px -1px 0 #333; }
  .coupon__terms {
    position: absolute; left: 175px; top: 6px; width: 275px; text-align: center;
    font-size: 13px; line-height: 17px; color: #fff;
  }
  .coupon__terms .deadline { display: block; font-weight: 700; margin-top: 1px; }
  .coupon__field { position: absolute; left: 215px; top: 62px; width: 170px; height: 20px; background: #fff; border-radius: 8px; }

  .footer {
    position: absolute; left: 0; bottom: 0; width: 530px; height: 100px;
    background: var(--card); display: flex; align-items: center; justify-content: space-between;
    padding: 0 22px 0 20px;
  }
  .footer__brand { font-family: "Open Sans", Arial, sans-serif; font-weight: 400; color: var(--brand-blue); font-size: 23px; }
  .footer__contact { text-align: right; }
  .footer__phone {
    display: flex; align-items: center; justify-content: flex-end; gap: 4px;
    font-family: "Open Sans", Arial, sans-serif; font-weight: 700; color: var(--alert-red); font-size: 25px; line-height: 30px;
  }
  .footer__web { font-weight: 700; color: var(--ink); font-size: 17px; }
</style>
</head>
<body>

<section class="postcard postcard--front">
  <div class="photo photo--before" role="img" aria-label="Shop window with property listings behind glass covered in scratches and etched graffiti"></div>
  <svg class="panel-curve" style="top:330px" width="530" height="62" viewBox="0 0 530 62" aria-hidden="true">
    <path d="M0 54 Q265 2 530 32 L530 62 L0 62 Z" fill="#f4f4f4"/>
    <path d="M0 54 Q265 2 530 32" fill="none" stroke="#2aa9e8" stroke-width="7"/>
  </svg>
  <svg class="pointer-arrow" viewBox="0 0 140 170" aria-hidden="true">
    <path d="M55 165 C15 130 20 70 80 45 L74 25 L135 48 L92 95 L88 75 C50 90 45 125 70 160 Z" fill="#e0161b" stroke="#fff" stroke-width="5" stroke-linejoin="round"/>
  </svg>
  <div class="stage-tag stage-tag--before">
    <div class="stage-tag__title">BEFORE REPAIR</div>
    <div class="stage-tag__sub">A bad first impression</div>
  </div>
  <h1 class="headline">
    <span class="headline__line">Don't let vandals</span>
    <span class="headline__line">Wreck your <span class="headline__accent">Image!</span></span>
  </h1>
  <p class="intro-box">What's on display in your shop window? If it's graffiti, vandalism, or just wear and tear, that's the first impression your customers get – <strong>and it's not good.</strong> Lucent Glass Repairs remove damage from glass windows, making them sparkling clear – without replacing the glass! Our glass repair work is effective, green, and very economical. See our coupon on the other side to save even more! <span class="call-line">Call now for expert advice: 0800 555 0147.</span></p>
  <footer class="footer">
    <span class="footer__brand">Lucent Glass Repairs</span>
    <div class="footer__contact">
      <div class="footer__phone">
        <svg width="22" height="22" viewBox="0 0 24 24" aria-hidden="true"><path d="M6.6 10.8c1.4 2.8 3.8 5.1 6.6 6.6l2.2-2.2c.3-.3.7-.4 1-.2 1.1.4 2.3.6 3.6.6.6 0 1 .4 1 1V20c0 .6-.4 1-1 1C10.6 21 3 13.4 3 4c0-.6.4-1 1-1h3.5c.6 0 1 .4 1 1 0 1.3.2 2.5.6 3.6.1.3 0 .7-.2 1z" fill="#1a1a1a"/></svg>
        0800 555 0147
      </div>
      <div class="footer__web">www.lucentglassrepairs.co.uk</div>
    </div>
  </footer>
</section>

<section class="postcard postcard--back">
  <div class="photo photo--after" role="img" aria-label="The same shop window after repair, glass clear with property listings visible"></div>
  <svg class="panel-curve" style="top:280px" width="530" height="60" viewBox="0 0 530 60" aria-hidden="true">
    <path d="M0 48 Q265 8 530 44 L530 60 L0 60 Z" fill="#f4f4f4"/>
    <path d="M0 48 Q265 8 530 44" fill="none" stroke="#2aa9e8" stroke-width="7"/>
  </svg>
  <div class="stage-tag stage-tag--after">
    <div class="stage-tag__title">AFTER REPAIR</div>
    <div class="stage-tag__sub">clear as new!</div>
  </div>
  <div class="benefits">
    <h2 class="benefits__title">WHY LUCENT GLASS REPAIRS?</h2>
    <ul class="benefits__list">
      <li>We repair most shop window glass! We repair laminated, tempered, toughened, mirrored, tinted, and even ballistic glass.</li>
      <li>We repair curved glass! Don't replace expensive curved panes – get the like‑new look for less by repairing.</li>
      <li>Finer work! We remove etched graffiti tags, scratches, mineral deposits, and acid etched graffiti damage .</li>
      <li>Edge expertise! We can repair even deep scratches as close as 20mm from the edge of the glass.</li>
      <li class="benefit--strong"><strong>Save time and money!</strong> Typical savings of up to 80% over the cost of glass replacement, with zero downtime during repair.</li>
    </ul>
  </div>
  <div class="coupon">
    <div class="coupon__badge"><span class="coupon__badge-save">SAVE</span> 20%</div>
    <p class="coupon__terms">off our regular prices for scratch repair, restoration, and etched graffiti removal.<span class="deadline">ACT NOW – OFFER EXPIRES</span></p>
    <div class="coupon__field"></div>
  </div>
  <footer class="footer">
    <span class="footer__brand">Lucent Glass Repairs</span>
    <div class="footer__contact">
      <div class="footer__phone">
        <svg width="22" height="22" viewBox="0 0 24 24" aria-hidden="true"><path d="M6.6 10.8c1.4 2.8 3.8 5.1 6.6 6.6l2.2-2.2c.3-.3.7-.4 1-.2 1.1.4 2.3.6 3.6.6.6 0 1 .4 1 1V20c0 .6-.4 1-1 1C10.6 21 3 13.4 3 4c0-.6.4-1 1-1h3.5c.6 0 1 .4 1 1 0 1.3.2 2.5.6 3.6.1.3 0 .7-.2 1z" fill="#1a1a1a"/></svg>
        0800 555 0147
      </div>
      <div class="footer__web">www.lucentglassrepairs.co.uk</div>
    </div>
  </footer>
</section>

</body>
</html>
```